brightvale7 Growers & Crafters Market Spring Festival

Harvest Festival Flyer. Bright Spring colors, Spring flowers, spring produce/food, Grass, Concert poster look, but legible...or MODERN LOOK- I am uploading Sponsor files that will go on bottom of flyer. I am uploading past flyers, and samples of other flyers that I like.
Flyer Info: 5x7 Size
When & Where:
April 19 9am-4pm
Marlow Commons 417 N. Bellhaven
What:
DIY workshops
Beer Truck
FREE Games & Prizes
Live Entertainment
Chef Demos
Peanut Eating Contest
FREE Kids Art Garden
BBQ
More info to come.....I have to finalize with vendors.
Sponsor Logos at Bottom:
Marlow Commons
Kikis smokehouse
brightvale7
Sol Dorado
Build Bright Paths
Green Thumb Guild
Updates

I have 2 more sponsor logos to upload.  Canine Coaching Pro & Ridgeway Brewing Company

Please add Easter Photos

please ad petting zoo

Target Market(s)

Adults 25-50

Industry/Entity Type

Festival

Requirements
Must have
• The list of items i listed above
Should not have
• County look.Make it modern

```html
<!DOCTYPE html>
<html lang="en">
<head>
<meta charset="utf-8">
<title>Harvest Festival</title>
<link rel="stylesheet" href="https://fonts.googleapis.com/css2?family=Fredoka:wght@500;600;700&display=swap">
<style>
  :root {
    --sun-light: #f4fbd2;
    --sun-mid: #c8ea62;
    --sun-edge: #7cc424;
    --leaf: #5fb31a;
    --leaf-dark: #2f7d0e;
    --orange: #f5821f;
    --cream: #ffffff;
    --ink: #2f5a10;
  }
  * { margin: 0; padding: 0; box-sizing: border-box; }
  html, body { width: 859px; height: 1200px; overflow: hidden; }
  body { font-family: "Fredoka", sans-serif; }
  .flyer {
    position: relative;
    width: 859px;
    height: 1200px;
    overflow: hidden;
    background: radial-gradient(circle at 50% 30%, var(--sun-light) 0%, var(--sun-mid) 45%, var(--sun-edge) 100%);
  }
  .flower-art {
    position: absolute;
    left: 40px;
    top: -30px;
    width: 780px;
    height: 600px;
    border-radius: 50%;
    background: radial-gradient(ellipse at 50% 45%, #fff6c9 0%, #ffe07a 30%, #f7b6c8 55%, rgba(95,179,26,0.8) 78%, rgba(95,179,26,0) 100%);
  }
  .title {
    position: absolute;
    left: 0;
    width: 100%;
    text-align: center;
    font-weight: 700;
    line-height: 1;
    white-space: nowrap;
    paint-order: stroke fill;
    -webkit-text-stroke: 14px var(--cream);
  }
  .title--harvest { top: 100px; font-size: 180px; color: var(--leaf); }
  .title--festival { top: 280px; font-size: 176px; color: var(--orange); }
  .when-where {
    position: absolute;
    left: 0;
    width: 100%;
    text-align: center;
    font-weight: 700;
    color: var(--leaf-dark);
    white-space: nowrap;
    paint-order: stroke fill;
    -webkit-text-stroke: 7px var(--cream);
    line-height: 1;
  }
  .when-where--date { top: 662px; font-size: 52px; }
  .when-where--place { top: 722px; font-size: 48px; }
  .activities {
    position: absolute;
    left: 40px;
    top: 790px;
    width: 780px;
    height: 182px;
    background: var(--orange);
    border: 4px solid var(--cream);
    border-radius: 6px;
    display: grid;
    grid-template-columns: 1fr 1fr;
    padding: 8px 0;
  }
  .activities__column {
    list-style: none;
    display: flex;
    flex-direction: column;
    justify-content: space-around;
    color: var(--cream);
    font-weight: 600;
    font-size: 30px;
    line-height: 1.1;
    white-space: nowrap;
    padding: 0 18px;
  }
  .activities__column--left { text-align: right; border-right: 4px solid var(--cream); }
  .sponsors-heading {
    position: absolute;
    left: 34px;
    top: 978px;
    font-size: 54px;
    line-height: 1;
    font-weight: 700;
    color: var(--orange);
    paint-order: stroke fill;
    -webkit-text-stroke: 7px var(--cream);
  }
  .sponsor-band {
    position: absolute;
    left: 0;
    bottom: 0;
    width: 100%;
    height: 150px;
    background: var(--cream);
    display: flex;
    align-items: center;
    justify-content: space-around;
    padding: 0 16px;
  }
  .sponsor {
    width: 128px;
    text-align: center;
    font-size: 22px;
    font-weight: 600;
    line-height: 1.1;
    color: var(--ink);
  }
</style>
</head>
<body>
  <main class="flyer">
    <div class="flower-art" role="img" aria-label="Spring flowers and grass illustration around the title"></div>

    <h1>
      <span class="title title--harvest">Harvest</span>
      <span class="title title--festival">Festival</span>
    </h1>

    <p class="when-where when-where--date">April 19 9am-4pm</p>
    <p class="when-where when-where--place">Marlow Commons 417 N. Bellhaven</p>

    <section class="activities">
      <ul class="activities__column activities__column--left">
        <li>DIY workshops</li>
        <li>Beer Truck</li>
        <li>FREE Games &amp; Prizes</li>
        <li>Live Entertainment</li>
      </ul>
      <ul class="activities__column activities__column--right">
        <li>Chef Demos</li>
        <li>Peanut Eating Contest</li>
        <li>FREE Kids Art Garden</li>
        <li>BBQ</li>
      </ul>
    </section>

    <h2 class="sponsors-heading">Sponsors:</h2>

    <footer class="sponsor-band">
      <span class="sponsor">Marlow Commons</span>
      <span class="sponsor">Kikis smokehouse</span>
      <span class="sponsor">brightvale7</span>
      <span class="sponsor">Sol Dorado</span>
      <span class="sponsor">Build Bright Paths</span>
      <span class="sponsor">Green Thumb Guild</span>
    </footer>
  </main>
</body>
</html>
```